Social Media Graphics - ALL TEXT KB

We are looking for a series of social media graphics for Instagram (standard size 1:1 (1080x1080px) that are ALL TEXT. We want the following quotes below on each graphic; one quote per graphic. AND, In very small letters at the bottom of each graphic, add @KBWardleOnline

The look and feel of these graphics should be complimentary to the color palette attached below; but keep them simple. But the design is up to you; at the end of this document, I provided various samples of all text graphics that I like as examples.

Target Market(s)

women looking to lose weight

Industry/Entity Type

health and wellness

Colors
E54698
E96AAD
F1A4CE
F9D9EA
FCEFF6

Requirements
Must have
• the quotes in the document
Should not have
• no stock photography

```html
<!DOCTYPE html>
<html lang="en">
<head>
<meta charset="utf-8">
<title>KB Wardle — Text Quote Graphics</title>
<link rel="stylesheet" href="https://fonts.googleapis.com/css2?family=Tinos&family=Poppins:wght@800&family=Parisienne&family=Roboto:wght@400;700&family=Montserrat:wght@600;700&display=swap">
<style>
  :root {
    --pink-deep: #d6046f;
    --pink-hot: #ff0a8a;
    --pink-rose: #e54698;
    --pink-mid: #e96aad;
    --pink-soft: #f1a4ce;
    --pink-pale: #f9d9ea;
    --pink-mist: #fcf0f6;
    --pink-quote: #ff5aa8;
    --ink: #1a1a1a;
    --white: #ffffff;
  }
  * { margin: 0; padding: 0; box-sizing: border-box; }
  html, body { width: 1200px; height: 269px; overflow: hidden; background: var(--white); }
  .canvas { position: relative; width: 1200px; height: 269px; }
  .tile { position: absolute; top: 26px; width: 216px; height: 216px; overflow: hidden; }

  .tile--soft { left: 25px;
    background:
      linear-gradient(160deg, rgba(233,106,173,.55) 0%, rgba(241,164,206,.35) 35%, rgba(255,255,255,0) 65%),
      linear-gradient(20deg, rgba(233,106,173,.35) 0%, rgba(255,255,255,0) 40%),
      radial-gradient(circle at 40% 75%, var(--white) 0%, var(--pink-pale) 45%, var(--pink-soft) 100%); }
  .tile--soft .quote { position: absolute; left: 19px; top: 61px; width: 190px;
    font-family: "Tinos", serif; font-size: 15px; line-height: 19.5px; color: var(--ink); }
  .tile--soft .handle { position: absolute; left: 19px; top: 148px;
    font-family: "Tinos", serif; font-size: 7px; color: var(--ink); }

  .tile--bold { left: 259px; background: var(--pink-hot); }
  .mark { position: absolute; font-family: "Poppins", sans-serif; font-weight: 800; color: var(--pink-quote); line-height: 1; }
  .mark--open { left: 12px; top: -6px; font-size: 64px; }
  .mark--close { right: 14px; bottom: -34px; font-size: 64px; }
  .tile--bold .quote { position: absolute; left: 20px; top: 57px; width: 192px;
    font-family: "Poppins", sans-serif; font-weight: 800; font-size: 13.4px; line-height: 21.5px; color: var(--white); text-transform: uppercase; }
  .tile--bold .handle { position: absolute; left: 22px; top: 147px;
    font-family: "Poppins", sans-serif; font-weight: 800; font-size: 8px; color: var(--white); }

  .tile--script { left: 492px; background: radial-gradient(ellipse at 50% 50%, var(--pink-rose) 0%, var(--pink-deep) 75%); }
  .tile--script .quote { position: absolute; left: 32px; top: 64px; width: 175px;
    font-family: "Parisienne", cursive; font-size: 16px; line-height: 21.5px; color: var(--white); }
  .tile--script .handle { position: absolute; left: 32px; top: 138px;
    font-family: "Parisienne", cursive; font-size: 10px; color: var(--white); }

  .tile--floral { left: 725px; background: var(--white); }
  .floral { position: absolute; background: radial-gradient(circle, var(--pink-pale) 0%, rgba(249,217,234,0) 75%); }
  .floral--top { left: 0; top: 0; width: 88px; height: 62px; }
  .floral--bottom { left: 138px; top: 150px; width: 78px; height: 66px; }
  .tile--floral .tick-mark { position: absolute; left: 107px; top: 58px; font-family: "Roboto", sans-serif; font-weight: 700; font-size: 12px; color: var(--pink-deep); }
  .tile--floral .quote { position: absolute; left: 0; top: 79px; width: 216px; text-align: center;
    font-family: "Roboto", sans-serif; font-weight: 700; font-size: 11px; line-height: 14.6px; color: var(--pink-deep); text-transform: uppercase; }
  .tile--floral .handle { position: absolute; left: 0; top: 130px; width: 216px; text-align: center;
    font-family: "Roboto", sans-serif; font-size: 5.5px; color: var(--pink-rose); }

  .tile--lined { left: 959px; background: var(--pink-deep); }
  .tile--lined .mark--center { position: absolute; left: 0; width: 216px; top: 16px; text-align: center;
    font-family: "Poppins", sans-serif; font-weight: 800; font-size: 30px; color: var(--white); line-height: 1; }
  .rule { position: absolute; left: 36px; width: 146px; height: 1px; background: var(--white); }
  .rule--top { top: 53px; }
  .rule--bottom { top: 163px; }
  .tile--lined .quote { position: absolute; left: 0; top: 62px; width: 216px; text-align: center;
    font-family: "Montserrat", sans-serif; font-weight: 600; font-size: 10.5px; line-height: 18.8px; letter-spacing: .3px;
    color: var(--pink-deep); -webkit-text-stroke: .6px var(--white); text-transform: uppercase; }
  .tile--lined .handle { position: absolute; left: 0; top: 143px; width: 216px; text-align: center;
    font-family: "Montserrat", sans-serif; font-weight: 700; font-size: 8px; color: var(--white); }
</style>
</head>
<body>
<main class="canvas">
  <section class="tile tile--soft">
    <p class="quote">Wake up tomorrow with a flatter belly- yes, this overnight remedy works like magic!</p>
    <p class="handle">- @KBWardleOnline</p>
  </section>

  <section class="tile tile--bold">
    <span class="mark mark--open">“</span>
    <p class="quote">Finally-a natural solution that flattens your bellyand eases stomach bloat</p>
    <p class="handle">- @KBWardleOnline</p>
    <span class="mark mark--close">”</span>
  </section>

  <section class="tile tile--script">
    <p class="quote">That stubborn belly fat isn't your fault here's what no one tells you</p>
    <p class="handle">KBWardleOnline</p>
  </section>

  <section class="tile tile--floral">
    <div class="floral floral--top" role="img" aria-label="Pink line-drawn flower sprig"></div>
    <span class="tick-mark">“</span>
    <p class="quote">You've been lied to - 'Just<br>eat less and exercise more'<br>doesn't work in menopause</p>
    <p class="handle">- @KBWardleOnline</p>
    <div class="floral floral--bottom" role="img" aria-label="Pink line-drawn flower sprig"></div>
  </section>

  <section class="tile tile--lined">
    <span class="mark--center">“</span>
    <span class="rule rule--top"></span>
    <p class="quote">Sis, your hormones<br>are out of whack –<br>that's why the weight<br>won't budge!</p>
    <p class="handle">- @KBWardleOnline</p>
    <span class="rule rule--bottom"></span>
  </section>
</main>
</body>
</html>
```